KESTREL BOILWORKS business card

We need a new business card for our company "Kestrel Boilworks". The company is very simple, we supply bulk heated water to the oilfield and industry. I have included a few images of cards that I like so that you have an idea of the direction I want to go. I will leave fonts up to the designer. I have also included our logo.
Updates

Hello Designers,  if there are any more submissions coming in you might consider using other background colors than black.  I am looking for a little bit of variety before making the decision.

Thanks,

Dean

Sorry, I meant to say background colors other than just black and white.

Thanks,

Dean

Target Market(s)

Ages 20 to 60. Oilfield consultants and Oil and Gas Companies

Industry/Entity Type

Business

Font styles to use
Sans Serif

Requirements
Must have
• Dean Varga

email info@kestrelboilworks-mail.com

Phone # 780-555-3817
Fax 780-555-2964

Site 317, Box 4, Comp 2, RR5
Drayton Valley, AB, T9K 4P3

11-07-52-3 W4M
Hwy 734 Between RR57 & RR58

**Must have our logo

Nice to have
• Would be nice to have " Bulk Heated Water" somewhere on the card

The logo with the flame large across the background might look ok? The name of the company is KESTREL BOILWORKS, but it probably isn't necessary to have the hot water under the logo all the time if you decide it looks better. As long as it is included somewhere on the card. The style of the Kestrel can change slightly (ie:; can be slanted).

The colors of the logo can change, but it might be nice to have the original color and logo somewhere small (corner?)

```html
<!DOCTYPE html>
<html lang="en">
<head>
<meta charset="utf-8">
<title>Kestrel Boilworks — Business Card</title>
<link rel="stylesheet" href="https://fonts.googleapis.com/css2?family=Source+Sans+3:wght@400;600;700;800&display=swap">
<style>
  :root {
    --backdrop: #6e6f71;
    --card-white: #f7f7f5;
    --card-deep: #163a5c;
    --ink: #2a2b2e;
    --brand-red: #e0312b;
    --brand-blue: #3f9bd0;
    --paper-white: #ffffff;
  }
  * { box-sizing: border-box; margin: 0; padding: 0; }
  html, body {
    width: 1200px; height: 780px; overflow: hidden;
    background: var(--backdrop);
    font-family: "Source Sans 3", "Helvetica Neue", Arial, sans-serif;
  }
  .stage {
    width: 1200px; height: 780px;
    display: flex; align-items: center; justify-content: center; gap: 40px;
  }
  .card {
    position: relative; width: 520px; height: 297px; overflow: hidden;
    box-shadow: 0 6px 18px rgba(0,0,0,.28);
  }

  /* Front */
  .card--front { background: var(--card-white); color: var(--ink); }
  .band { position: absolute; background: var(--brand-blue); }
  .band--top-right { top: 0; right: 0; width: 118px; height: 22px; }
  .band--bottom-left { bottom: 0; left: 0; width: 210px; height: 22px; }
  .band--left-edge { bottom: 0; left: 0; width: 14px; height: 96px; }

  .tagline {
    position: absolute; top: 34px; right: 40px;
    color: var(--brand-red); font-weight: 800; font-size: 12px; letter-spacing: .06em;
  }
  .brand {
    position: absolute; top: 44px; left: 36px;
    display: flex; align-items: center; gap: 10px;
  }
  .brand__dot { width: 22px; height: 22px; border-radius: 50%; background: var(--brand-blue); }
  .brand__name { color: var(--brand-red); font-weight: 800; font-size: 17px; letter-spacing: .04em; line-height: 1; }

  .person {
    position: absolute; top: 84px; left: 40px;
    font-size: 18px; font-weight: 700; color: var(--ink); line-height: 1;
  }

  .contact {
    position: absolute; top: 118px; left: 40px;
    display: grid; grid-template-columns: 66px auto; row-gap: 2px;
    font-size: 17px; line-height: 1.15;
  }
  .contact__label, .contact__value { color: var(--ink); }

  .divider {
    position: absolute; top: 200px; left: 40px; right: 40px;
    border-top: 1.5px dashed var(--brand-red);
  }
  .address {
    position: absolute; top: 210px; left: 70px;
    font-style: normal; font-size: 14px; line-height: 1.35; color: var(--ink);
  }
  .address__line--legal { padding-left: 40px; }

  /* Back */
  .card--back { background: var(--card-deep); display: flex; align-items: center; justify-content: center; }
  .backmark { display: flex; align-items: center; gap: 22px; }
  .backmark__disc { width: 120px; height: 120px; border-radius: 50%; background: var(--brand-blue); }
  .backmark__name { color: var(--paper-white); font-weight: 800; font-size: 50px; letter-spacing: .05em; line-height: 1; }
</style>
</head>
<body>
<main class="stage">
  <section class="card card--front" aria-label="Business card front">
    <div class="band band--top-right"></div>
    <div class="band band--bottom-left"></div>
    <div class="band band--left-edge"></div>

    <p class="tagline">BULK HEATED WATER</p>

    <div class="brand">
      <span class="brand__dot"></span>
      <span class="brand__name">KESTREL BOILWORKS</span>
    </div>

    <p class="person">Dean Varga</p>

    <dl class="contact">
      <dt class="contact__label">Email</dt><dd class="contact__value">info@kestrelboilworks-mail.com</dd>
      <dt class="contact__label">Phone</dt><dd class="contact__value">780-555-3817</dd>
      <dt class="contact__label">Fax</dt><dd class="contact__value">780-555-2964</dd>
    </dl>

    <div class="divider"></div>

    <address class="address">
      <div class="address__line">Site 317, Box 4, Comp 2, RR5, Drayton Valley, AB, T9K 4P3</div>
      <div class="address__line address__line--legal">11-07-52-3 W4M - Hwy 734 Between RR57 &amp; RR58</div>
    </address>
  </section>

  <section class="card card--back" aria-label="Business card back">
    <div class="backmark">
      <span class="backmark__disc"></span>
      <span class="backmark__name">KESTREL</span>
    </div>
  </section>
</main>
</body>
</html>
```